KELBRO INSULATION WEB PAGE
WEB PAGE
THANK YOU VELNOX MEDIA,AND THANK YOU TO ALL WHO PARTICIPATE.....GRACIAS
appreciate morel
I like the concept of a picture of a dream home,but i also like the stock picture on draft #31,because it tells you that can be a new but also show you the attic and it looks like a remodeling
Morel,
Thank you for giving me 4stars this is a original size which you will see on wide screen.
Many Thanks.
Hey Morel,
I have done few changes in my design please have a look and give me feedback & if you need any changes please let me know.
morel,
I will do changes as you mention and submit my draft again.
I do like what he wrote on draft # 16 and I like the colors and all the contents in draft # 18
Hi PH,
I am inn, design will submit soon.....Thanks
what happend with the drafts for fossils? i hope that you sen more the first ones were good
Can you upload your logo?
I THINK I DID HAVE A MISTAKE,I WANT THE URL TO BE " kelbroinsulation.com "i was thinking that you were asking for websites that i like.

```html
<!DOCTYPE html>
<html lang="en">
<head>
<meta charset="utf-8">
<title>Kelbro Insulation</title>
<link href="https://fonts.googleapis.com/css2?family=Questrial&family=Arimo:ital,wght@0,400;1,700&display=swap" rel="stylesheet">
<style>
:root{
  --page:#ececec;
  --white:#ffffff;
  --green:#2f8a2a;
  --green-dark:#1f6b1c;
  --green-light:#7fcf3a;
  --lime:#a6d81e;
  --yellow:#ffd21a;
  --yellow-light:#fff27a;
  --text:#444444;
  --muted:#8a8a8a;
  --rule:#d6d6d6;
  --sky-top:#c9dbe8;
  --sky-low:#a9b9c6;
  --sea:#6f8191;
}
*{margin:0;padding:0;box-sizing:border-box}
html,body{width:1200px;height:1052px;overflow:hidden;background:var(--page)}
body{position:relative;font-family:"Questrial",sans-serif;color:var(--text)}
.site{position:absolute;left:134px;top:0;width:932px;height:905px;background:var(--white)}
.brand{position:absolute;left:0;top:0;width:256px;height:162px;
  background:linear-gradient(180deg,var(--yellow-light) 0%,var(--yellow) 100%);
  display:flex;align-items:center;gap:12px;padding-left:18px}
.brand-mark{width:34px;height:34px;background:var(--green);flex:none}
.brand-name{font-family:"Questrial",sans-serif;font-size:23px;color:var(--green-dark);line-height:1.05;letter-spacing:1px}
.phones{position:absolute;right:48px;top:10px;font-size:11px;color:var(--muted);display:flex;gap:12px;align-items:center}
.phones svg{width:10px;height:10px}
.hero{position:absolute;left:256px;top:28px;width:676px;height:461px;
  background:linear-gradient(180deg,var(--sky-top) 0%,var(--sky-low) 62%,var(--sea) 100%)}
.tagline-band{position:absolute;left:256px;top:489px;width:676px;height:46px;
  background:linear-gradient(90deg,var(--white) 0%,#cfe8c0 35%,var(--green) 75%,var(--green-dark) 100%);
  display:flex;align-items:center;justify-content:flex-end;padding-right:20px}
.tagline{font-family:"Arimo",sans-serif;font-style:italic;font-weight:700;font-size:17px;color:var(--yellow);letter-spacing:.5px}
.nav{position:absolute;left:0;top:162px;width:256px;height:373px;background:var(--green);list-style:none;padding-top:36px}
.nav li{position:relative;height:64px;display:flex;align-items:center;padding-left:88px;
  color:var(--white);font-size:15px;border-bottom:1px solid rgba(255,255,255,.25);margin:0 14px 0 14px;padding-right:20px}
.nav li:last-child{border-bottom:none}
.nav li svg{position:absolute;right:6px;width:14px;height:20px}
.nav li.current{height:42px;margin:0 20px 10px 22px;padding-left:72px;border:none;border-radius:6px;
  background:linear-gradient(180deg,#c9f07a 0%,var(--green-light) 55%,#5fb52a 100%);color:var(--green-dark);font-weight:bold}
.nav li.current svg{right:-26px}
.columns{position:absolute;left:0;top:535px;width:932px;height:370px;display:flex}
.col{width:311px;padding:26px 26px 0 26px;border-left:1px solid var(--rule)}
.col:first-child{border-left:none}
.col h2{font-weight:400;font-size:22px;color:var(--muted);text-align:center;margin-bottom:18px}
.lead{font-family:"Arimo",sans-serif;font-style:italic;font-weight:700;font-size:13px;line-height:1.3;color:var(--green-dark);margin-bottom:24px}
.col p.body{font-size:12px;line-height:1.35;color:var(--text);margin-bottom:22px}
.contact-box{position:absolute;left:770px;top:805px;width:290px;height:86px;background:var(--green);padding:10px 14px}
.contact-box h3{font-weight:400;font-size:12px;color:var(--white);margin-bottom:8px}
.contact-row{display:flex;gap:8px}
.contact-input{width:172px;height:30px;background:var(--white)}
.contact-submit{width:80px;height:30px;background:var(--lime);color:var(--green-dark);font-size:14px;display:flex;align-items:center;justify-content:center}
.footer{position:absolute;left:0;top:920px;width:1200px;text-align:center;color:#666;font-size:17px}
.footer-links{display:flex;justify-content:center;gap:0}
.footer-links span{padding:0 16px;border-left:1px solid #666;line-height:1}
.footer-links span:first-child{border-left:none}
.copyright{margin-top:10px;font-size:16px}
</style>
</head>
<body>
<div class="site">
  <div class="brand">
    <div class="brand-mark"></div>
    <div class="brand-name">KELBRO<br>INSULATION</div>
  </div>
  <div class="phones">
    <svg viewBox="0 0 10 10"><circle cx="5" cy="5" r="5" fill="#ffd21a"/></svg>
    <span>0100-555-0147</span><span>0100-555-0182</span>
  </div>
  <div class="hero" role="img" aria-label="Photo of a hand holding a small model house above the sea under a soft sky"></div>
  <div class="tagline-band"><span class="tagline">VALUE ADD INSULATION</span></div>
  <ul class="nav">
    <li class="current">Home<svg viewBox="0 0 14 20"><path d="M3 2l8 8-8 8" fill="none" stroke="#fff" stroke-width="3"/></svg></li>
    <li>Services<svg viewBox="0 0 14 20"><path d="M3 2l8 8-8 8" fill="none" stroke="#fff" stroke-width="3"/></svg></li>
    <li>Projects<svg viewBox="0 0 14 20"><path d="M3 2l8 8-8 8" fill="none" stroke="#fff" stroke-width="3"/></svg></li>
    <li>Clients<svg viewBox="0 0 14 20"><path d="M3 2l8 8-8 8" fill="none" stroke="#fff" stroke-width="3"/></svg></li>
    <li>Contact Us<svg viewBox="0 0 14 20"><path d="M3 2l8 8-8 8" fill="none" stroke="#fff" stroke-width="3"/></svg></li>
  </ul>
  <div class="columns">
    <section class="col">
      <h2>Welcome</h2>
      <p class="lead">We pride ourselves on providing unsurpassed service to a wide range of builders.</p>
      <p class="body">Insulation was established in 1983 by Dale and Nora Quimby. Providing old-fashioned customer service, with an eye on the future to deliver fresh ideas that will generate comfort and savings for families</p>
      <p class="body">Insulation was established in 1983 by Dale and Nora Quimby. Providing old-fashioned customer service, with an eye on the future to deliver fresh ideas that will generate comfort and savings for families</p>
    </section>
    <section class="col">
      <h2>New Projects</h2>
      <p class="lead">Each client and their project is our number one concern.</p>
      <p class="body">Insulation was established in 1983 by Dale and Nora Quimby. Providing old-fashioned customer service, with an eye on the future to deliver fresh ideas that will generate comfort and savings for families</p>
      <p class="body">Insulation was established in 1983 by Dale and Nora Quimby. Providing old-fashioned customer service, with an eye on the future to deliver fresh ideas that will generate comfort and savings for families</p>
    </section>
    <section class="col">
      <h2>Latest News</h2>
      <p class="lead">Each client and their project is our number one concern.</p>
      <p class="body">Insulation was established in 1983 by Dale and Nora Quimby. Providing old-fashioned customer service, with an eye on the future to deliver fresh ideas that will generate comfort and savings for families</p>
    </section>
  </div>
</div>
<div class="contact-box">
  <h3>Contact Us Now!!</h3>
  <div class="contact-row"><div class="contact-input"></div><div class="contact-submit">Submit</div></div>
</div>
<footer class="footer">
  <div class="footer-links"><span>Home</span><span>Services</span><span>Projects</span><span>Clients</span><span>Contact Us</span></div>
  <div class="copyright">Copyright© 2010 &nbsp;kelbroinsulation.com</div>
</footer>
</body>
</html>
```